body therapist

I need to offer my services as a massage therapist at home, acclimating customer space aroma candles with music and everything else to bring comfort. 8 offer rituals like this: relaxing ritual, purifying ritual, ritual breast, facial and body cleansing ritual organic, ritual man, ritual feet, slimming ritual. Naraja handling colors, seawater, green, lavender

Target Market(s)

men and women, tired, stressed, looking for something new

Font styles to use
Decorative
Script

Colors
f37122
0493ce
abd037

Requirements
Must have
• detailing each massage
Nice to have
• simple and elegant

```html
<!DOCTYPE html>
<html lang="en">
<head>
<meta charset="utf-8">
<title>Serena Touch – Massage Therapist at Home</title>
<link rel="stylesheet" href="https://fonts.googleapis.com/css2?family=Roboto+Condensed:wght@400;700&family=Roboto:wght@400;500&display=swap">
<style>
  :root{
    --orange:#f37122;
    --blue:#0493ce;
    --green:#abd037;
    --green-deep:#8fbc24;
    --ink:#1d1d1d;
    --paper:#ffffff;
    --backdrop:#ececec;
  }
  *{box-sizing:border-box;margin:0;padding:0}
  html,body{width:1200px;height:752px;overflow:hidden}
  body{background:var(--backdrop);font-family:"Roboto",Arial,sans-serif;position:relative}

  .poster{
    position:absolute;left:350px;top:22px;width:500px;height:707px;
    background:var(--paper);overflow:hidden;
    box-shadow:0 4px 18px rgba(0,0,0,.18);
  }

  /* hero photo and curves */
  .hero-photo{
    position:absolute;left:0;top:60px;width:500px;height:340px;
    background:
      radial-gradient(ellipse 120px 90px at 440px 60px,#7fae4a 0%,rgba(127,174,74,0) 100%),
      radial-gradient(ellipse 160px 120px at 330px 110px,#d9b39a 0%,rgba(217,179,154,0) 100%),
      radial-gradient(ellipse 220px 130px at 190px 230px,#e2b999 0%,rgba(226,185,153,0) 100%),
      linear-gradient(180deg,#e9ddd2 0%,#d8b49a 55%,#f1ece6 100%);
  }
  .hero-curves{position:absolute;left:0;top:0;width:500px;height:470px}

  .brand{position:absolute;left:14px;top:0;width:200px;height:135px}
  .brand-mark{
    position:absolute;left:56px;top:0;width:90px;height:90px;
    border:2px solid var(--green);border-radius:50%;
  }
  .brand-name{
    position:absolute;left:0;top:98px;width:200px;text-align:center;
    font-family:"Roboto Condensed",Arial,sans-serif;font-weight:700;
    font-size:28px;line-height:1;color:var(--green-deep);
  }

  .headline{
    position:absolute;right:12px;top:340px;text-align:right;
    font-family:"Roboto Condensed",Arial,sans-serif;font-weight:700;color:var(--paper);
    text-shadow:1px 1px 0 var(--orange),-1px 1px 0 var(--orange),2px 2px 0 var(--orange);
    line-height:1;
  }
  .headline-main{display:block;font-size:52px}
  .headline-sub{display:block;font-size:38px;margin-top:0}

  .tagline{
    position:absolute;left:0;top:437px;width:500px;height:23px;
    background:var(--orange);color:var(--paper);
    font-size:15px;line-height:23px;text-align:center;
  }

  .offer{
    position:absolute;left:0;top:460px;width:500px;height:61px;
    background:var(--green);
    font-family:"Roboto Condensed",Arial,sans-serif;font-weight:700;
    font-size:29px;line-height:61px;text-align:center;color:var(--orange);
    text-shadow:1px 1px 0 #fff,-1px -1px 0 #fff,1px -1px 0 #fff,-1px 1px 0 #fff,2px 2px 0 #fff;
  }

  .rituals{
    position:absolute;left:0;top:521px;width:500px;height:81px;
    padding-top:7px;text-align:center;color:var(--orange);
    font-size:15px;line-height:22.5px;
    border-top:1px solid var(--orange);
  }
  .rituals-rule{position:absolute;left:0;top:602px;width:500px;height:2px;background:var(--orange)}

  .contact{
    position:absolute;left:0;top:604px;width:232px;height:77px;
    background:linear-gradient(90deg,var(--green) 80%,#c9e07e 100%);
    padding:18px 0 0 60px;color:var(--ink);font-size:12px;line-height:15px;
  }
  .spa-photo{
    position:absolute;left:232px;top:604px;width:268px;height:77px;
    background:
      radial-gradient(ellipse 60px 20px at 60px 60px,#f2a31c 0%,rgba(242,163,28,0) 100%),
      radial-gradient(ellipse 110px 30px at 170px 40px,#5a4a42 0%,rgba(90,74,66,0) 100%),
      linear-gradient(180deg,#e4c7b0 0%,#d7a988 60%,#f4efe9 100%);
  }
  .web{
    position:absolute;left:0;top:681px;width:500px;height:26px;
    background:var(--blue);color:var(--paper);
    font-size:11px;letter-spacing:3px;line-height:26px;text-align:center;
  }
</style>
</head>
<body>
  <main class="poster">
    <div class="hero-photo" role="img" aria-label="Photo of a couple relaxing side by side while receiving a shoulder massage"></div>

    <svg class="hero-curves" viewBox="0 0 500 470" aria-hidden="true">
      <path d="M0 0 H500 V74 C360 92 190 140 0 180 Z" fill="#ffffff"/>
      <path d="M0 184 C190 144 360 96 500 78" fill="none" stroke="var(--orange)" stroke-width="9"/>
      <path d="M0 400 C150 398 320 330 500 318 V470 H0 Z" fill="var(--green)"/>
      <path d="M0 396 C150 394 320 326 500 314" fill="none" stroke="var(--blue)" stroke-width="5"/>
      <path d="M0 389 C150 386 320 316 500 304" fill="none" stroke="var(--orange)" stroke-width="8"/>
    </svg>

    <div class="brand">
      <span class="brand-mark"></span>
      <span class="brand-name">Serena Touch</span>
    </div>

    <h1 class="headline">
      <span class="headline-main">Massage</span>
      <span class="headline-sub">Therapist at home</span>
    </h1>

    <p class="tagline">aroma candles with music and everything else to bring comfort</p>

    <h2 class="offer">8 OFFER RITUALS</h2>

    <p class="rituals">
      relaxing ritual | purifying ritual | ritual breast<br>
      facial and body cleansing ritual organic | ritual man | ritual feet<br>
      slimming ritual | Naraja handling colors | seawater | green | lavender
    </p>
    <div class="rituals-rule"></div>

    <address class="contact" style="font-style:normal">
      0000 111 222<br>
      Your Address<br>
      youremail@here.com
    </address>
    <div class="spa-photo" role="img" aria-label="Photo of a woman relaxing during a hot stone massage with flowers"></div>

    <p class="web">yourwebsite@here.com</p>
  </main>
</body>
</html>
```